ORBIT conference Slide Deck

This is a conference for our team that will be 3 days of discussions on how to build our business in the middle of these challenging time. Its a bit of a battle and so we are going with a red and grey/black these although I am open to your interpretation. I will include a few graphics that we have started on to show you the look. But I am just getting started, INSPIRE ME! The screen will be 100' across the front of the room and these decks will show on each side and I will reformat for the middle 1X6 screen as needed. I have the AI file of the logo if you need it. I don't see where to upload it here.

Target Market(s)

our top producers

Industry/Entity Type

Real Estate Agent

Font styles to use
Sans Serif

Colors
ec1f27

Requirements
Must have
• Depth, creativity

```html
<!DOCTYPE html>
<html lang="en">
<head>
<meta charset="UTF-8">
<title>ORBIT Conference – Speaker Slide</title>
<link href="https://fonts.googleapis.com/css2?family=Montserrat:ital,wght@0,400;0,700;0,800;1,600&display=swap" rel="stylesheet">
<style>
  :root {
    --paper: #f3f3f3;
    --ink: #000000;
    --charcoal: #231f20;
    --signal-red: #ec1f27;
    --white: #ffffff;
    --photo-warm: #8a4a22;
    --photo-light: #e9e6e2;
  }
  html, body {
    margin: 0;
    padding: 0;
    overflow: hidden;
    background: var(--paper);
  }
  .slide {
    position: relative;
    width: 1200px;
    height: 675px;
    overflow: hidden;
    background: var(--paper);
    font-family: "Montserrat", Arial, sans-serif;
  }
  .backdrop {
    position: absolute;
    inset: 0;
    width: 1200px;
    height: 675px;
  }
  .speaker-photo {
    position: absolute;
    left: 158px;
    top: 143px;
    width: 220px;
    height: 220px;
    border-radius: 50%;
    background:
      radial-gradient(circle at 45% 45%, var(--photo-light) 0 38%, #cfc9c2 55%, transparent 70%),
      linear-gradient(120deg, #c9a27c 0%, var(--photo-warm) 60%, #5b2d12 100%);
  }
  .speaker {
    position: absolute;
    left: 0;
    width: 527px;
    top: 418px;
    text-align: center;
    color: var(--charcoal);
  }
  .speaker-name {
    margin: 0;
    font-weight: 800;
    font-size: 24px;
    letter-spacing: 0.12em;
    line-height: 30px;
  }
  .speaker-role {
    margin: 0;
    font-weight: 400;
    font-size: 22px;
    letter-spacing: 0.07em;
    line-height: 28px;
  }
  .title-bracket {
    position: absolute;
    left: 0;
    top: 0;
    width: 1200px;
    height: 675px;
  }
  .headline {
    position: absolute;
    left: 640px;
    top: 160px;
    margin: 0;
    color: var(--white);
    font-weight: 800;
    font-size: 39px;
    line-height: 46px;
    letter-spacing: 0.11em;
  }
  .body-copy {
    position: absolute;
    left: 641px;
    top: 344px;
    width: 302px;
    margin: 0;
    color: var(--white);
    font-weight: 600;
    font-style: italic;
    font-size: 22.5px;
    line-height: 33.6px;
    letter-spacing: 0.05em;
  }
  .body-copy .line { display: block; white-space: nowrap; }
  .body-copy .line--justified { text-align: justify; text-align-last: justify; white-space: normal; }
  .event-mark {
    position: absolute;
    left: 1113px;
    top: 489px;
    transform: translate(-50%, -50%) rotate(-90deg);
    color: var(--signal-red);
    font-weight: 700;
    font-size: 90px;
    line-height: 1;
    letter-spacing: 0.01em;
    white-space: nowrap;
  }
</style>
</head>
<body>
  <main class="slide">
    <svg class="backdrop" viewBox="0 0 1200 675" aria-hidden="true">
      <polygon fill="var(--ink)" points="564,0 1200,0 1200,675 508,675 525,475 554,451 530,419"/>
    </svg>

    <div class="speaker-photo" role="img" aria-label="Speaker portrait photo"></div>

    <div class="speaker">
      <p class="speaker-name">JANE SMITH</p>
      <p class="speaker-role">THIS ROLE, THAT PLACE</p>
    </div>

    <svg class="title-bracket" viewBox="0 0 1200 675" aria-hidden="true">
      <polyline fill="none" stroke="var(--signal-red)" stroke-width="7.5" stroke-linejoin="miter"
        points="732,144.5 616,144.5 616,269.5 725,269.5 729,252"/>
    </svg>

    <h1 class="headline">LOREM IPSUM<br>DOLOR SIT</h1>

    <p class="body-copy">
      <span class="line line--justified">Lorem ipsum dolor sit</span>
      <span class="line line--justified">massa, elit adipiscing</span>
      <span class="line">consectetuer. Du Fusce</span>
      <span class="line">posuere, magna et sed</span>
      <span class="line">pulvinar ultricies, puru</span>
      <span class="line">lectus libero quis urna.</span>
    </p>

    <div class="event-mark">ORBIT</div>
  </main>
</body>
</html>
```